Poster for Network Documentary

I am doing a documentary about the history of America and how it has caused the events that led to the Social Justice Movement in 2020. Need a cover that illustrates that. The title HARVEST 9.0 - "The Quiet Tide". I will need to hand off the editable .psd design to a 3-D animator to create a 5sec bump. Let me know if you need additional direction.

Target Market(s)

Streamora, KLT, WZQ documentaries, MOXA

Industry/Entity Type

Film Production

Font styles to use
Sans Serif

Requirements
Must have
• Bold, Broadcast Network, captivating look
Nice to have
• Bold dynamic text. Should clearly communicate that it's a powerful documentary about the bad history of the USA and the social justice movement of 2020.

```html
<!DOCTYPE html>
<html lang="en">
<head>
<meta charset="utf-8">
<title>HARVEST 9.0 - The Quiet Tide</title>
<link rel="stylesheet" href="https://fonts.googleapis.com/css2?family=Alfa+Slab+One&family=Russo+One&display=swap">
<style>
  :root {
    --bg-light: #d6dedb;
    --bg-mid: #aab7b4;
    --bg-dark: #6d7876;
    --edge: #262522;
    --ink-white: #ffffff;
    --flag-red: #c8232c;
    --flag-blue: #1f3a7a;
    --flag-white: #f4f4f4;
    --crowd-glow: #f1e6cd;
    --crowd-warm: #b88a5e;
    --crowd-mid: #7d5a3f;
    --crowd-dark: #3a302a;
  }
  html, body {
    margin: 0;
    padding: 0;
    overflow: hidden;
    background: var(--edge);
  }
  .poster {
    position: relative;
    width: 890px;
    height: 1200px;
    overflow: hidden;
    background:
      radial-gradient(ellipse 30% 18% at 14% 6%, rgba(38, 37, 34, 0.7) 0%, rgba(38, 37, 34, 0) 100%),
      radial-gradient(ellipse 22% 14% at 30% 12%, rgba(60, 58, 54, 0.35) 0%, rgba(60, 58, 54, 0) 100%),
      radial-gradient(ellipse 26% 20% at 90% 10%, rgba(60, 66, 64, 0.35) 0%, rgba(60, 66, 64, 0) 100%),
      radial-gradient(ellipse 70% 55% at 50% 60%, var(--bg-light) 0%, var(--bg-mid) 58%, var(--bg-dark) 100%);
  }
  .poster::after {
    content: "";
    position: absolute;
    inset: 0;
    box-shadow: inset 0 0 90px 18px rgba(30, 29, 26, 0.8);
    pointer-events: none;
  }
  .crowd-photo {
    position: absolute;
    left: 0;
    top: 740px;
    width: 890px;
    height: 460px;
    background:
      radial-gradient(ellipse 26% 34% at 50% 22%, var(--crowd-glow) 0%, rgba(241, 230, 205, 0) 100%),
      radial-gradient(ellipse 16% 40% at 14% 58%, rgba(125, 90, 63, 0.9) 0%, rgba(125, 90, 63, 0) 100%),
      radial-gradient(ellipse 14% 38% at 34% 55%, rgba(184, 138, 94, 0.85) 0%, rgba(184, 138, 94, 0) 100%),
      radial-gradient(ellipse 14% 38% at 68% 55%, rgba(184, 138, 94, 0.85) 0%, rgba(184, 138, 94, 0) 100%),
      radial-gradient(ellipse 16% 40% at 86% 58%, rgba(125, 90, 63, 0.9) 0%, rgba(125, 90, 63, 0) 100%),
      linear-gradient(180deg, rgba(184, 138, 94, 0) 0%, rgba(184, 138, 94, 0.55) 28%, var(--crowd-mid) 62%, var(--crowd-dark) 100%);
  }
  .title-block {
    position: absolute;
    left: 0;
    top: 0;
    width: 890px;
    height: 760px;
  }
  .title-word,
  .tagline {
    font-family: "Alfa Slab One", "Rockwell", serif;
    fill: var(--ink-white);
  }
  .title-number {
    font-family: "Russo One", "Arial Black", sans-serif;
  }
</style>
</head>
<body>
<main class="poster">
  <div class="crowd-photo" role="img" aria-label="Photograph of raised clenched fists of a crowd, backlit by warm light"></div>
  <svg class="title-block" width="890" height="760" viewBox="0 0 890 760" aria-label="HARVEST 9.0 — The Quiet Tide">
    <defs>
      <linearGradient id="number-fill" x1="0" y1="0" x2="1" y2="1">
        <stop offset="0" stop-color="var(--flag-blue)"/>
        <stop offset="0.38" stop-color="var(--flag-blue)"/>
        <stop offset="0.5" stop-color="var(--flag-white)"/>
        <stop offset="0.62" stop-color="var(--flag-red)"/>
        <stop offset="1" stop-color="var(--flag-red)"/>
      </linearGradient>
    </defs>
    <rect class="title-rule" x="145" y="172" width="608" height="13" fill="var(--ink-white)"/>
    <text class="title-word" x="149" y="338" font-size="196" textLength="600" lengthAdjust="spacingAndGlyphs">HARVEST</text>
    <rect class="title-rule" x="145" y="356" width="608" height="13" fill="var(--ink-white)"/>
    <text class="title-number" x="148" y="608" font-size="296" textLength="605" lengthAdjust="spacingAndGlyphs" fill="url(#number-fill)" stroke="#ffffff" stroke-width="2">9.0</text>
    <text class="tagline" x="449" y="716" font-size="86" text-anchor="middle" textLength="620" lengthAdjust="spacingAndGlyphs">“The Quiet Tide”</text>
  </svg>
</main>
</body>
</html>
```